Tall Harbor Business Card

We are a Video Production and Video Equipment Rental company specialising in the supply of state of the art Video Technology and Services for the Live Entertainment, Television and Corporate Business Theatre markets. (in Sydney, Australia) www.tallharbor-media.example

Industry/Entity Type

Business

Contact Information for Business Card

name, position, email, website, address, logo
Example attached of the information we need - doesn't necessarily have to look the same

Font styles to use
Other font styles liked:
• Tall Harbor logo font is GOTHAM

Colors
ea1f27

Requirements
Nice to have
• either matt black or shiny black cards -
raised logo

```html
<!DOCTYPE html>
<html lang="en">
<head>
<meta charset="utf-8">
<title>Tall Harbor Business Card</title>
<link href="https://fonts.googleapis.com/css2?family=Oswald:wght@300;400;500&display=swap" rel="stylesheet">
<style>
  :root {
    --brand-red: #ea1f27;
    --ink: #141414;
    --paper: #fdfaf9;
    --backdrop: #e9e9e9;
    --on-red: #ffffff;
  }
  * { margin: 0; padding: 0; box-sizing: border-box; }
  html, body {
    width: 1200px;
    height: 800px;
    overflow: hidden;
    background: var(--backdrop);
  }
  .card {
    position: absolute;
    left: 120px;
    top: 100px;
    width: 960px;
    height: 600px;
    display: flex;
    font-family: "Oswald", "Arial Narrow", sans-serif;
    color: var(--ink);
  }
  .card__contact {
    position: relative;
    width: 395px;
    height: 100%;
    background: var(--paper);
  }
  .card__brand {
    position: relative;
    flex: 1;
    height: 100%;
    background: var(--brand-red);
  }
  .contact-line {
    position: absolute;
    right: 134px;
    font-weight: 400;
    font-size: 20px;
    line-height: 1.15;
    letter-spacing: 0.03em;
    text-align: right;
    text-transform: uppercase;
  }
  .contact-line--email { top: 86px; }
  .contact-line--web { top: 159px; }
  .contact-line--address { top: 228px; }
  .contact-icon {
    position: absolute;
    left: 278px;
    width: 30px;
    height: 30px;
  }
  .contact-icon--email { top: 88px; }
  .contact-icon--web { top: 160px; }
  .contact-icon--pin { top: 226px; }
  .person {
    position: absolute;
    right: 102px;
    top: 388px;
    text-align: right;
    text-transform: uppercase;
  }
  .person__name {
    font-weight: 400;
    font-size: 50px;
    line-height: 1;
    letter-spacing: 0.03em;
  }
  .person__role {
    margin-top: 8px;
    font-weight: 400;
    font-size: 22px;
    letter-spacing: 0.03em;
  }
  .accent-bar {
    position: absolute;
    left: 0;
    bottom: 0;
    width: 166px;
    height: 32px;
    background: var(--brand-red);
  }
  .brand-name {
    position: absolute;
    left: 42px;
    top: 222px;
    width: 489px;
    height: 119px;
    display: flex;
    align-items: center;
    justify-content: center;
    gap: 22px;
    color: var(--on-red);
    font-weight: 400;
    font-size: 64px;
    letter-spacing: 0.04em;
    text-transform: uppercase;
  }
  .brand-name__square {
    width: 22px;
    height: 22px;
    background: var(--on-red);
  }
  .tagline {
    position: absolute;
    left: 50px;
    top: 350px;
    width: 474px;
    color: var(--on-red);
    font-weight: 400;
    font-size: 17.5px;
    letter-spacing: 0.02em;
    text-align: center;
    text-transform: uppercase;
    white-space: nowrap;
  }
</style>
</head>
<body>
  <article class="card">
    <section class="card__contact">
      <p class="contact-line contact-line--email">rae@tallharbor-media.example</p>
      <svg class="contact-icon contact-icon--email" viewBox="0 0 30 30" aria-hidden="true">
        <rect x="3" y="7" width="24" height="16" fill="none" stroke="var(--brand-red)" stroke-width="2"/>
        <path d="M3 7 L15 17 L27 7 M3 23 L12 14.5 M27 23 L18 14.5" fill="none" stroke="var(--brand-red)" stroke-width="2"/>
      </svg>

      <p class="contact-line contact-line--web">www.tallharbor-media.example</p>
      <svg class="contact-icon contact-icon--web" viewBox="0 0 30 30" aria-hidden="true">
        <g fill="none" stroke="var(--brand-red)" stroke-width="1.6">
          <circle cx="15" cy="15" r="12"/>
          <ellipse cx="15" cy="15" rx="5.5" ry="12"/>
          <line x1="3" y1="15" x2="27" y2="15"/>
          <path d="M5 9 H25 M5 21 H25"/>
        </g>
      </svg>

      <address class="contact-line contact-line--address" style="font-style:normal">
        12 Wharf Lane<br>Marrick NSW 2099<br>Australia
      </address>
      <svg class="contact-icon contact-icon--pin" viewBox="0 0 30 30" aria-hidden="true">
        <path d="M15 2 C9.5 2 6.5 6 6.5 10.5 C6.5 17 15 28 15 28 C15 28 23.5 17 23.5 10.5 C23.5 6 20.5 2 15 2 Z" fill="var(--brand-red)"/>
        <circle cx="15" cy="10.5" r="3" fill="var(--paper)"/>
      </svg>

      <div class="person">
        <h1 class="person__name">Rae Calloway</h1>
        <p class="person__role">Managing Director</p>
      </div>

      <div class="accent-bar"></div>
    </section>

    <section class="card__brand">
      <div class="brand-name">
        <span class="brand-name__square"></span>
        <span>Tall Harbor</span>
      </div>
      <p class="tagline">Video Solutions - LED Screens - Camera Systems - Projection</p>
    </section>
  </article>
</body>
</html>
```